Homebuilder & Remodeling Firm looking for archectrual looking website

We are a Custom home building & remodeling company since 1986 and would like to launch a website.Carl Tondevik the principle of the firm is a graduate of Harwell Univesity school of architecture and draws his own designs and working drawings. and has done many residential, single and multi family projects in the Dallas Ft Worth Metroplex. We want our website to be architectural in design and visually appealing. We will eventually have photos to provide for you. The message we want to communicate is we have current update knowledge with trends, and longevity in experience. Our message is that we are a firm that designs and remodels fully through and we provide a well executed custom home that is unique to each client. The Homes that we build are unique ,authentic and sustainable architectural styles such as mid century modern, contemporary, transitional and they are sophisticated homes to compliment individual lifestyles of our clients. We have a passion for construction and an attention to detail that makes your dreams come to life. We listen to each clients every need in functionality and form and take them from pre-construction to post-construction follow -up.
We help you invest in your home. Thoughts Create Reality

EXAMPLES OF WEBSITES THAT WE LIKE. PLEASE DO
MORE CONTEMPORARY, SLEEK, ARCHITECTURAL

* Please make the LOGO a bigger part of design

http://pellamcrew.build/
https://www.vintrasol.co/
http://dostavanehomes.com/
http://www.milesfardowdesign.com/
http://www.quillmerton.com/
http://fennikdesignstudios.com/about
http://brandelorgc.com/

thank you,

Reason: We have many clients asking to see our website and re ready to launch something for them to look at

Target Market(s)

Home owners, home buyers, interior designers, All ages

Industry/Entity Type

Builders

Coding

Coded - Design and coding required

Number of Pages Required

5+ page

Font styles to use
Sans Serif

Requirements
Must have
• HTML5 OR PHP
• graphic artist must speak English:
• *Visually appealing, user friendly,
• * the website should reflect the stability and integrity of the company since it has been in business for over 30 years
• * a sophistication and refinement is our mandate.
Should not have
• Too busy, too much going on, we want more minimal in design and artsitic

```html
<!DOCTYPE html>
<html lang="en">
<head>
<meta charset="utf-8">
<title>Tondevik Development</title>
<link href="https://fonts.googleapis.com/css2?family=Fira+Sans:wght@300;400;500&display=swap" rel="stylesheet">
<style>
:root{
  --navy:#1b2d57;
  --navy-soft:#5d76b3;
  --ink:#333;
  --muted:#6b6b6b;
  --gold:#a5772f;
  --panel:#f3f3f3;
  --line:#e4e4e4;
  --white:#fff;
  --black:#0b0b0b;
}
*{box-sizing:border-box;margin:0;padding:0}
html,body{width:1200px;height:2913px;overflow:hidden;background:var(--white)}
body{position:relative;font-family:"Fira Sans",sans-serif;color:var(--ink)}
.abs{position:absolute}
/* sidebar */
.sidebar{left:0;top:0;width:301px;height:2913px;background:var(--white)}
.brand{left:32px;top:52px;display:flex;align-items:center;gap:10px}
.brand-mark{width:30px;height:30px;background:var(--navy)}
.brand-name{font-size:17px;font-weight:400;color:var(--navy);letter-spacing:.4px;line-height:1}
.brand-tag{font-size:7px;letter-spacing:2px;color:var(--muted);margin-top:4px}
.nav{left:18px;top:110px;width:264px;list-style:none}
.nav li{height:49px;border-bottom:1px solid var(--line);display:flex;align-items:center;justify-content:center;font-size:12px;letter-spacing:4px;color:var(--gold)}
.nav li.active{color:var(--navy);font-weight:500}
.social{left:0;width:301px;top:459px;display:flex;justify-content:center;gap:20px}
.social span{width:11px;height:11px;border-radius:50%;background:var(--navy)}
/* hero */
.hero{left:301px;top:0;width:899px;height:561px;background:
  radial-gradient(ellipse 60% 40% at 45% 20%,rgba(230,170,90,.85),transparent 70%),
  radial-gradient(ellipse 50% 30% at 80% 90%,rgba(150,120,40,.6),transparent 70%),
  linear-gradient(180deg,#1a1410 0%,#6b4a26 30%,#c4873c 55%,#4a3420 80%,#120d08 100%)}
.hero-title{left:524px;top:204px;width:451px;height:126px;background:rgba(20,18,16,.78);color:var(--white);text-align:center;font-size:36px;font-weight:400;letter-spacing:9px;line-height:46px;padding-top:17px}
/* why */
.why-photo{left:301px;top:561px;width:373px;height:464px;background:
  radial-gradient(ellipse 70% 30% at 50% 75%,rgba(70,190,230,.8),transparent 70%),
  linear-gradient(180deg,#2c3a22 0%,#3f7a3a 35%,#2b6e5a 55%,#2a86b0 72%,#14283c 100%)}
.why-panel{left:674px;top:561px;width:526px;height:464px;background:var(--panel)}
.why-panel h2{position:absolute;left:89px;top:96px;font-size:26px;font-weight:400;color:#222}
.why-panel p{position:absolute;left:89px;width:400px;font-size:12.5px;line-height:21px;color:var(--muted);font-weight:300}
/* services */
.section-title{width:899px;left:301px;text-align:center;font-size:27px;font-weight:400;color:#222}
.dot{width:5px;height:5px;background:#222;border-radius:50%}
.card-img{top:1225px;height:134px}
.card h3{position:absolute;top:1388px;font-size:15px;font-weight:400;color:#333}
.card p{position:absolute;top:1421px;width:280px;font-size:12.5px;line-height:21px;color:var(--muted);font-weight:300}
.band{left:301px;width:899px;background:var(--navy)}
.btn{border:1.5px solid var(--white);color:var(--white);font-size:13px;letter-spacing:2px;display:flex;align-items:center;justify-content:center;gap:14px}
/* filters */
.filters{top:1705px;left:449px;display:flex;gap:6px}
.filters span{height:33px;padding:0 20px;border:1.5px solid var(--navy);display:flex;align-items:center;font-size:11px;letter-spacing:3px;color:#444}
.filters span.on{background:var(--navy);color:var(--white)}
.tile{height:197px}
/* testimonials */
.testimonials{left:301px;top:2301px;width:899px;height:534px;background:
  radial-gradient(ellipse 30% 40% at 85% 30%,rgba(200,170,120,.35),transparent 70%),
  linear-gradient(90deg,#2a241e 0%,#4a4036 40%,#5a5044 60%,#2e2822 100%)}
.t-title{left:301px;width:899px;top:2376px;text-align:center;color:var(--white);font-size:28px;font-weight:400}
.t-rule{left:473px;top:2441px;width:555px;height:1px;background:rgba(255,255,255,.25)}
.quote{top:2499px;width:330px;height:214px;background:rgba(34,31,29,.85)}
.quote .q{position:absolute;left:0;top:12px;width:48px;height:32px;background:var(--navy);color:#8ea0c9;font-size:26px;text-align:center;line-height:40px;font-family:Georgia,serif}
.quote p{position:absolute;left:68px;top:14px;width:240px;color:var(--white);font-size:12.5px;line-height:21px;font-weight:300}
.quote .who{position:absolute;left:68px;top:180px;color:var(--navy-soft);font-size:12.5px;font-weight:400}
.pager{top:2738px;left:739px;display:flex;gap:8px}
.pager span{width:5px;height:5px;border-radius:50%;background:rgba(255,255,255,.5)}
.pager span.on{background:var(--white)}
.footer{left:301px;top:2835px;width:899px;height:78px;background:var(--black);color:var(--white);font-size:13px;font-weight:300}
.footer .copy{position:absolute;left:73px;top:31px}
.footer .copy b{color:var(--gold);font-weight:300}
.footer .fsocial{position:absolute;right:86px;top:34px;display:flex;gap:20px}
.footer .fsocial span{width:11px;height:11px;border-radius:50%;background:var(--gold)}
</style>
</head>
<body>

<aside class="abs sidebar">
  <div class="abs brand">
    <div class="brand-mark"></div>
    <div>
      <div class="brand-name">TONDEVIK DEVELOPMENT</div>
      <div class="brand-tag">CUSTOM HOMES &amp; REMODELING</div>
    </div>
  </div>
  <ul class="abs nav">
    <li class="active">HOME</li>
    <li>ABOUT US</li>
    <li>OUR STORY</li>
    <li>OUR SERVICES</li>
    <li>AVAILABLE NOW</li>
    <li>CONTACT US</li>
  </ul>
  <div class="abs social" aria-label="Social links"><span></span><span></span><span></span><span></span><span></span></div>
</aside>

<section class="abs hero" role="img" aria-label="Night photograph of a curved modern building canopy lit in warm gold"></section>
<h1 class="abs hero-title">TONDEVIK<br>DEVELOPMENT</h1>

<div class="abs why-photo" role="img" aria-label="Photograph of a lit pool courtyard between residential towers with palms"></div>
<section class="abs why-panel">
  <h2>WHY CHOOSE TONDEVIK</h2>
  <p style="top:160px">Interior design is the art or process of designing the interior, often including the exterior, of a room or building. An interior designer is someone who coordinates and manages such projects.</p>
  <p style="top:238px">Interior design is a multifaceted profession that includes conceptual development, communicating with the stakeholders of a project and the management and execution of the design. Lorem ipsum dolor sit amet, consectetur adipisicing elit, sed do eiusmod tempor incididunt ut labore et dolore magna aliqua. Ut enim ad minim veniam, quis nostrud exercitation ullamco laboris nisi ut aliquip ex ea commodo consequat.</p>
</section>

<h2 class="abs section-title" style="top:1104px">OUR SERVICES</h2>
<div class="abs dot" style="left:748px;top:1167px"></div>

<div class="card">
  <div class="abs card-img" style="left:301px;width:280px;background:linear-gradient(100deg,#f1ede6 0%,#d8cfc0 40%,#b08b52 65%,#6a5134 100%)" role="img" aria-label="Photograph of a reading nook with a wooden lounge chair"></div>
  <h3 style="left:301px">Town Home Design</h3>
  <p style="left:301px">Sed ut perspiciatis unde omnis iste natus error volupt atem accusan tium dolore mque laudan omnis.</p>
</div>
<div class="card">
  <div class="abs card-img" style="left:608px;width:283px;background:linear-gradient(180deg,#f4f2ee 0%,#e6e2da 45%,#c4824a 70%,#9a5e30 100%)" role="img" aria-label="Photograph of a bright stairwell with an orange sofa"></div>
  <h3 style="left:608px">Mid Rise Design</h3>
  <p style="left:608px">Sed ut perspiciatis unde omnis iste natus error volupt atem accusan tium dolore mque laudan omnis.</p>
</div>
<div class="card">
  <div class="abs card-img" style="left:917px;width:279px;background:linear-gradient(100deg,#5d5346 0%,#e8e3da 35%,#c9b28a 60%,#7a5c38 100%)" role="img" aria-label="Photograph of a study corner with shelving and a lounge chair"></div>
  <h3 style="left:917px">Multi Use Design</h3>
  <p style="left:917px">Sed ut perspiciatis unde omnis iste natus error volupt atem accusan tium dolore mque laudan omnis.</p>
</div>

<div class="abs band" style="top:1511px;height:142px"></div>
<div class="abs btn" style="left:643px;top:1563px;width:213px;height:36px">VIEW ALL SERVICES
  <svg width="9" height="13" viewBox="0 0 9 13"><path d="M2 1.5l5 5-5 5" stroke="#fff" stroke-width="2.5" fill="none"/></svg></div>

<div class="abs filters">
  <span class="on">ALL</span><span>COMMERCIAL</span><span>HOSPITALITY</span><span>OFFICE</span><span>RESIDENTIAL</span>
</div>

<div class="abs tile" style="left:301px;top:1765px;width:294px;background:linear-gradient(100deg,#eeeae2 0%,#cfc4b0 35%,#a67e48 65%,#4c3b2a 100%)" role="img" aria-label="Project photograph: living room with wooden chair"></div>
<div class="abs tile" style="left:595px;top:1765px;width:296px;background:linear-gradient(180deg,#6e6b66 0%,#b8b3aa 35%,#f2f0ec 65%,#2a2622 100%)" role="img" aria-label="Project photograph: hotel bedroom with white bed"></div>
<div class="abs tile" style="left:891px;top:1765px;width:299px;background:linear-gradient(180deg,#d4dfe8 0%,#a9b4bc 40%,#5a4c44 70%,#2b221d 100%)" role="img" aria-label="Project photograph: lounge with leather armchairs and glazed ceiling"></div>
<div class="abs tile" style="left:301px;top:1962px;width:294px;background:linear-gradient(180deg,#c4bc98 0%,#8a7a58 40%,#d8d2c6 65%,#1e1a16 100%)" role="img" aria-label="Project photograph: modern bedroom with low bed"></div>
<div class="abs tile" style="left:595px;top:1962px;width:296px;background:linear-gradient(135deg,#5a5a5a 0%,#bdbdbd 45%,#d8d6d2 60%,#3e3a36 100%)" role="img" aria-label="Project photograph: office meeting room with wood table"></div>
<div class="abs tile" style="left:891px;top:1962px;width:299px;background:linear-gradient(180deg,#8a5228 0%,#c98a50 40%,#e0b480 65%,#6a3c1c 100%)" role="img" aria-label="Project photograph: restaurant with timber slatted ceiling"></div>

<div class="abs band" style="top:2159px;height:142px"></div>
<div class="abs btn" style="left:641px;top:2210px;width:219px;height:37px">VIEW ALL PROJECTS
  <svg width="9" height="13" viewBox="0 0 9 13"><path d="M2 1.5l5 5-5 5" stroke="#fff" stroke-width="2.5" fill="none"/></svg></div>

<section class="abs testimonials" role="img" aria-label="Dimmed photograph of a warm-toned interior room"></section>
<h2 class="abs t-title">CUSTOMER SAYS</h2>
<div class="abs t-rule"></div>
<div class="abs quote" style="left:402px">
  <div class="q">&ldquo;</div>
  <p>I have very much enjoyed with your services. Lorem ipsum dolor sit amet, consectetur adipisicing elit, sed do eiusmod tempor incididunt ut labore et dolore magna aliqua. Ut enim ad minim veniam, quis nostrud exercitation ullamco laboris nisi ut aliquip.</p>
  <div class="who">James, Customer</div>
</div>
<div class="abs quote" style="left:759px">
  <div class="q">&ldquo;</div>
  <p>I totally recommend your services. Lorem ipsum dolor sit amet, consectetur adipisicing elit, sed do eiusmod tempor incididunt ut labore et dolore magna aliqua. Ut enim ad minim veniam, quis nostrud exercitation ullamco laboris nisi ut aliquip.</p>
  <div class="who">Patrick, Customer</div>
</div>
<div class="abs pager"><span class="on"></span><span></span></div>

<footer class="abs footer">
  <div class="copy">&copy; Copyright 2017 <b>Tondevik Development</b>. All Rights Reserved.</div>
  <div class="fsocial" aria-label="Social links"><span></span><span></span><span></span><span></span><span></span></div>
</footer>

</body>
</html>
```